Housecleaning advertisement

We are a professional residential housecleaning service, in business since 2005, providing detailed, eco-friendly housecleaning to our clients. We are looking for a design that can be used in monthly coupon books ( 4c), quarterly local magazine (biz card sized 4c) and weekly newspaper ad (biz card sized b/w). We are looking for a retro feel - think 1940s kitchens - yellow, turquoise, bright red. we want to stress that we are a local firm, not a one-size fits all franchise. We provide very personalized service (linen changes, pet-friendly, flexible scheduling, sit down with customer prior to initial cleaning and discuss their priorities so that we know what they are looking for and deliver 110% each and every clean to them - and a a very reasonable price.) Our logo is a red car with two cleaners in it. Text for the ad :
Relax and enjoy your sparkling, clean, ready-for-company home!
Test drive our detailed, eco-friendly housecleaning
four hours for $100 (new clients only)
some bulleted points
* 100% Woman-owned and staffed. We know how to clean and tidy up - and treat your home with care and respect.
* Eco-friendly products - healthier for you and your family
* Fully insured and bonded.
415.382.9156
www.tidywrenhaus.net
Target Market(s)
Professional women ages 30-65 in the New Haven County, Ct market
Industry/Entity Type
Residential
Requirements
Nice to have
- retro 1940s 1950s

```html
<!DOCTYPE html>
<html lang="en">
<head>
<meta charset="utf-8">
<title>Tidy Wren Haus Housecleaning – Ad</title>
<link rel="stylesheet" href="https://fonts.googleapis.com/css2?family=Arimo:ital,wght@0,400;0,700;1,400&family=Lobster&display=swap">
<style>
  :root {
    --page: #e9e6df;
    --stripe-light: #ffffff;
    --stripe-blue: #cfe5ef;
    --oval-cream: #fbf3c8;
    --oval-rim: #8b7a3c;
    --retro-red: #d52a2a;
    --retro-blue: #2e8cc8;
    --cocoa: #7a4a1e;
    --ink: #3b2f22;
    --white: #ffffff;
  }
  html, body {
    margin: 0;
    width: 1200px;
    height: 900px;
    overflow: hidden;
    background: var(--page);
  }
  .ad-card {
    position: absolute;
    left: 75px;
    top: 150px;
    width: 1050px;
    height: 600px;
    background: repeating-linear-gradient(90deg,
      var(--stripe-light) 0 38px, var(--stripe-blue) 38px 76px);
    box-shadow: 0 6px 18px rgba(0,0,0,.25);
    overflow: hidden;
    font-family: "Arimo", Arial, sans-serif;
    color: var(--ink);
  }
  .oval-frame { position: absolute; left: 0; top: 0; }
  .call-badge {
    position: absolute;
    left: 12px; top: 70px;
    width: 132px; height: 132px;
    border-radius: 50%;
    background: var(--retro-red);
    border: 5px solid var(--white);
    box-shadow: 0 2px 6px rgba(0,0,0,.3);
    display: flex; align-items: center; justify-content: center;
    text-align: center;
    font-family: "Lobster", cursive;
    color: var(--white);
    font-size: 30px; line-height: 1.05;
    transform: rotate(-12deg);
  }
  .brand-name {
    position: absolute;
    left: 80px; width: 900px; top: 68px;
    text-align: center;
    font-weight: 700;
    font-size: 34px;
    line-height: 40px;
    color: var(--retro-red);
    margin: 0;
  }
  .tagline {
    position: absolute;
    left: 80px; width: 900px; top: 116px;
    text-align: center;
    font-family: "Lobster", cursive;
    font-size: 28px; line-height: 1.2;
    color: var(--cocoa);
    margin: 0;
  }
  .tagline em { font-style: normal; color: var(--retro-red); }
  .offer-box {
    position: absolute;
    left: 190px; top: 196px;
    width: 640px;
    padding: 10px 20px;
    background: var(--retro-blue);
    color: var(--white);
    font-size: 21px; line-height: 1.3;
    text-align: center;
  }
  .offer-box strong { font-weight: 700; }
  .perk-list {
    position: absolute;
    left: 215px; top: 296px;
    width: 395px;
    margin: 0; padding: 0;
    list-style: none;
  }
  .perk { position: relative; padding-left: 34px; margin-bottom: 8px; }
  .perk::before {
    content: "★";
    position: absolute; left: 0; top: -2px;
    color: var(--retro-red);
    font-size: 24px;
  }
  .perk-title {
    font-family: "Lobster", cursive;
    color: var(--retro-red);
    font-size: 22px;
    display: block;
  }
  .perk-note { font-size: 14px; color: var(--ink); display: block; }
  .logo-art {
    position: absolute;
    left: 625px; top: 300px;
    width: 205px; height: 145px;
    border-radius: 36px 36px 18px 18px;
    background: linear-gradient(160deg, #f4c84a 0%, #e2453a 55%, #2e8cc8 100%);
  }
  .contact-band {
    position: absolute;
    left: 0; right: 0; bottom: 0;
    height: 62px;
    background: var(--retro-blue);
    color: var(--white);
    display: flex; align-items: center; justify-content: space-between;
    padding: 0 60px;
    font-size: 26px; font-weight: 700;
  }
</style>
</head>
<body>
  <article class="ad-card">
    <svg class="oval-frame" width="1050" height="600" viewBox="0 0 1050 600" aria-hidden="true">
      <ellipse cx="530" cy="270" rx="470" ry="250" fill="var(--oval-cream)" stroke="var(--oval-rim)" stroke-width="7"/>
      <ellipse cx="530" cy="270" rx="456" ry="236" fill="none" stroke="var(--oval-rim)" stroke-width="2"/>
    </svg>

    <div class="call-badge">Call<br>Today!</div>

    <h1 class="brand-name">Tidy Wren Haus Housecleaning</h1>
    <p class="tagline">Relax and enjoy your sparkling, clean,<br><em>ready-for-company</em> home!</p>

    <div class="offer-box">
      <strong>Test drive</strong> our detailed, eco-friendly housecleaning<br>
      four hours for <strong>$100</strong> (new clients only)
    </div>

    <ul class="perk-list">
      <li class="perk">
        <span class="perk-title">100% Woman-owned and staffed!</span>
        <span class="perk-note">We know how to clean and tidy up – and treat your home with care and respect.</span>
      </li>
      <li class="perk">
        <span class="perk-title">Eco-friendly products</span>
        <span class="perk-note">Healthier for you and your family</span>
      </li>
      <li class="perk">
        <span class="perk-title">Fully insured and bonded.</span>
      </li>
    </ul>

    <div class="logo-art" role="img" aria-label="Logo illustration: red retro car with two cleaners riding in it"></div>

    <footer class="contact-band">
      <span class="phone">415.382.9156</span>
      <span class="web">www.tidywrenhaus.net</span>
    </footer>
  </article>
</body>
</html>
```